Business Card Design

We need a business card designed for our new company. Prefer a black card with white logo & writing.

Contact Information for Business Card

Dale Pickett, address: 7-4417 Larchmere Avenue, Abbotsford, BC, V3K 2R9, Office Phone: 604-555-0172, Cell: 604-555-0138, Email: dale@kelsoncoatworks.ca

Colors

Designer to choose only greyscale colors for use in the design.

```html
<!DOCTYPE html>
<html lang="en">
<head>
<meta charset="utf-8">
<title>Kelson Coatworks — Business Card</title>
<link rel="stylesheet" href="https://fonts.googleapis.com/css2?family=Montserrat:wght@400;500;600;700&display=swap">
<style>
  :root {
    --page: #ffffff;
    --card: #000000;
    --ridge-dark: #121212;
    --ridge-mid: #1d1d1d;
    --ridge-light: #2a2a2a;
    --ink: #ffffff;
    --ink-soft: #e8e8e8;
  }
  * { box-sizing: border-box; margin: 0; padding: 0; }
  html, body {
    width: 675px; height: 1200px; overflow: hidden;
    background: var(--page);
    font-family: "Montserrat", Arial, sans-serif;
    color: var(--ink);
  }
  .sheet {
    width: 675px; height: 1200px;
    display: flex; flex-direction: column; align-items: center; justify-content: center;
    gap: 48px;
  }
  .card {
    position: relative;
    width: 560px; height: 319px;
    background: var(--card);
    overflow: hidden;
  }
  .card__backdrop {
    position: absolute; inset: 0;
    background:
      radial-gradient(ellipse 60% 85% at 58% 100%, var(--ridge-light) 0%, var(--ridge-mid) 45%, transparent 80%),
      linear-gradient(180deg, var(--card) 0%, var(--ridge-dark) 55%, var(--ridge-mid) 100%);
  }
  .card__backdrop--back {
    background:
      radial-gradient(ellipse 62% 90% at 55% 100%, var(--ridge-light) 0%, var(--ridge-mid) 45%, transparent 80%),
      linear-gradient(180deg, var(--card) 0%, var(--ridge-dark) 55%, var(--ridge-mid) 100%);
  }

  /* Front */
  .front__rule {
    position: absolute; left: 47px; top: 0; bottom: 0;
    width: 1.5px; background: var(--ink);
  }
  .front__name {
    position: absolute; left: 81px; top: 30px;
    font-size: 21px; font-weight: 600; letter-spacing: 0.2px;
  }
  .contacts {
    position: absolute; left: 37px; top: 181px;
    list-style: none;
  }
  .contacts__item {
    display: flex; align-items: center;
    height: 20px; margin-bottom: 10.5px;
  }
  .contacts__icon {
    width: 20px; height: 20px; border-radius: 50%;
    background: var(--ink);
    display: flex; align-items: center; justify-content: center;
    flex: none;
  }
  .contacts__icon svg { width: 11px; height: 11px; fill: var(--card); }
  .contacts__text {
    margin-left: 24px;
    font-size: 15px; font-weight: 400; letter-spacing: 0.3px;
    color: var(--ink-soft);
  }
  .front__brand {
    position: absolute; left: 306px; top: 144px; width: 210px;
    text-align: center;
  }

  /* Brand wordmark */
  .brand {
    display: flex; align-items: center; justify-content: center; gap: 8px;
    font-weight: 700; font-size: 22px; letter-spacing: 0.5px;
    text-transform: uppercase; line-height: 1;
  }
  .brand__dot {
    width: 10px; height: 10px; border-radius: 50%;
    background: var(--ink); flex: none;
  }

  /* Back */
  .back__brand {
    position: absolute; left: 0; right: 0; top: 110px;
  }
  .back__company {
    position: absolute; left: 0; right: 0; top: 257px;
    text-align: center; font-size: 14px; font-weight: 600; letter-spacing: 0.4px;
  }
  .back__address {
    position: absolute; left: 0; right: 0; top: 276px;
    text-align: center; font-size: 14px; font-weight: 400; letter-spacing: 0.3px;
  }
</style>
</head>
<body>
<main class="sheet">

  <section class="card card--front" aria-label="Business card front">
    <div class="card__backdrop" role="img" aria-label="Dark grey silhouette of a mountain range behind the card content"></div>
    <div class="front__rule"></div>
    <h1 class="front__name">Dale Pickett</h1>
    <ul class="contacts">
      <li class="contacts__item">
        <span class="contacts__icon">
          <svg viewBox="0 0 24 24" aria-hidden="true"><path d="M3 9c0-2 4-4 9-4s9 2 9 4v1.5h-5V8.5H8v2H3z M6 12h12l2 7H4z M12 13.5a2.5 2.5 0 1 0 0 5a2.5 2.5 0 0 0 0-5z"/></svg>
        </span>
        <span class="contacts__text">604-555-0172</span>
      </li>
      <li class="contacts__item">
        <span class="contacts__icon">
          <svg viewBox="0 0 24 24" aria-hidden="true"><path d="M6.6 10.8a15.1 15.1 0 0 0 6.6 6.6l2.2-2.2c.3-.3.7-.4 1-.2 1.1.4 2.3.6 3.6.6.6 0 1 .4 1 1V20c0 .6-.4 1-1 1A17 17 0 0 1 3 4c0-.6.4-1 1-1h3.5c.6 0 1 .4 1 1 0 1.3.2 2.5.6 3.6.1.3 0 .7-.2 1z"/></svg>
        </span>
        <span class="contacts__text">604-555-0138</span>
      </li>
      <li class="contacts__item">
        <span class="contacts__icon">
          <svg viewBox="0 0 24 24" aria-hidden="true"><path d="M3 5h18v14H3z M4.5 6.5 12 12.5l7.5-6z" fill-rule="evenodd"/></svg>
        </span>
        <span class="contacts__text">dale@kelsoncoatworks.ca</span>
      </li>
    </ul>
    <div class="front__brand">
      <div class="brand"><span class="brand__dot"></span>Kelson Coatworks</div>
    </div>
  </section>

  <section class="card card--back" aria-label="Business card back">
    <div class="card__backdrop card__backdrop--back" role="img" aria-label="Dark grey silhouette of a mountain range filling the card"></div>
    <div class="back__brand">
      <div class="brand"><span class="brand__dot"></span>Kelson Coatworks</div>
    </div>
    <p class="back__company">KELSON COATWORKS</p>
    <p class="back__address">7-4417 Larchmere Avenue, Abbotsford, BC, V3K 2R9</p>
  </section>

</main>
</body>
</html>
```